Dornick and Associates Business Card

A business card that can be templates for all employees using our newly created logo and information. We are looking for stylish however simplistic in nature, clean looks are better than over the top, however creativity will be appreciated if it has the right appeal. Note: If you feel a type of card (plastic, metalic, carbon, raised lettering, etc) helps your design please specify.
Target Market(s)
Investigation ETC
Industry/Entity Type
Private Investigator
Contact Information for Business Card
Len Dornick
President
5173 Wexbury Road
Larkmoor Valley 00390-4412
Cell: 555-201-0193; Office: 555-201-0147
Email: lendornick@dornickassociates.example
Font styles to use
Requirements
Must have
- Website DornickAssociates.example
- Name, address, phone number ETC
- Use of current Logo and color pallets if applicable
- TM By logo, small

Nice to have
- Would like to see with and without a photo on the design

Should not have
- Redesign of logo, changing of colors

```html
<!DOCTYPE html>
<html lang="en">
<head>
<meta charset="utf-8">
<title>Dornick and Associates Business Card</title>
<link rel="stylesheet" href="https://fonts.googleapis.com/css2?family=Open+Sans:wght@400;700&display=swap">
<style>
  :root {
    --page: #ecebe8;
    --card-white: #f7f7f6;
    --card-dark: #4a4b4d;
    --orange-deep: #d9401c;
    --orange: #e8571f;
    --orange-light: #f39a2a;
    --text-light: #ffffff;
    --text-logo: #e24a1e;
    --text-logo-dark: #f07a3a;
  }
  * { margin: 0; padding: 0; box-sizing: border-box; }
  html, body { width: 1200px; height: 780px; overflow: hidden; }
  body {
    background: var(--page);
    font-family: "Open Sans", Arial, sans-serif;
    position: relative;
  }
  .card {
    position: absolute;
    top: 235px;
    width: 540px;
    height: 309px;
    border-radius: 4px;
    overflow: hidden;
    box-shadow: 0 6px 18px rgba(0,0,0,0.18);
  }
  .card-front { left: 40px; background: var(--card-white); }
  .card-back { left: 620px; background: var(--card-dark); }

  .accent-panel {
    position: absolute;
    top: 0; right: 0; bottom: 0;
    width: 250px;
    background: linear-gradient(120deg, var(--orange-light), var(--orange) 55%, var(--orange-deep));
  }
  .base-band {
    position: absolute;
    left: 0; right: 0; bottom: 0;
    height: 22px;
    background: var(--orange-deep);
  }

  .brand {
    position: absolute;
    display: flex;
    align-items: center;
    gap: 12px;
  }
  .brand-mark {
    width: 24px; height: 24px;
    border-radius: 50%;
    background: var(--text-logo);
    flex: none;
  }
  .brand-name {
    font-weight: 700;
    font-size: 24px;
    line-height: 1.1;
    color: var(--text-logo);
    text-transform: uppercase;
    letter-spacing: 0.5px;
  }
  .card-front .brand { left: 32px; top: 118px; }
  .card-front .brand-name { width: 200px; }
  .card-back .brand { left: 0; right: 0; top: 92px; justify-content: center; }
  .card-back .brand-mark { background: var(--text-logo-dark); }
  .card-back .brand-name { color: var(--text-logo-dark); font-size: 28px; width: 220px; }

  .contact {
    position: absolute;
    right: 20px;
    top: 30px;
    width: 226px;
    text-align: right;
    color: var(--text-light);
  }
  .contact-name { font-weight: 700; font-size: 20px; line-height: 1.1; }
  .contact-title { font-size: 12px; margin-bottom: 12px; }
  .contact-line {
    display: flex;
    justify-content: flex-end;
    align-items: center;
    gap: 6px;
    font-size: 10.5px;
    line-height: 18px;
    white-space: nowrap;
  }
  .contact-icon { width: 12px; height: 12px; flex: none; }

  .address-band {
    position: absolute;
    left: 0; right: 0; bottom: 34px;
    height: 40px;
    background: linear-gradient(90deg, var(--orange-deep), var(--orange) 50%, var(--orange-deep));
    display: flex;
    align-items: center;
    justify-content: center;
    color: var(--text-light);
    font-size: 14px;
  }
</style>
</head>
<body>

<section class="card card-front">
  <div class="accent-panel" role="img" aria-label="Decorative orange gradient artwork area"></div>
  <div class="base-band"></div>

  <div class="brand">
    <span class="brand-mark"></span>
    <span class="brand-name">Dornick and Associates</span>
  </div>

  <div class="contact">
    <div class="contact-name">Len Dornick</div>
    <div class="contact-title">President</div>
    <div class="contact-line">555-201-0193
      <svg class="contact-icon" viewBox="0 0 12 12"><rect x="3" y="0.5" width="6" height="11" rx="1" fill="none" stroke="#fff"/></svg>
    </div>
    <div class="contact-line">555-201-0147
      <svg class="contact-icon" viewBox="0 0 12 12"><path d="M2 1 L4.5 1 L5.5 3.5 L4 4.5 Q5 7 7.5 8 L8.5 6.5 L11 7.5 L11 10 Q5 11 1 2 Z" fill="#fff"/></svg>
    </div>
    <div class="contact-line">lendornick@dornickassociates.example
      <svg class="contact-icon" viewBox="0 0 12 12"><rect x="0.5" y="2.5" width="11" height="7" fill="none" stroke="#fff"/><path d="M0.5 2.5 L6 7 L11.5 2.5" fill="none" stroke="#fff"/></svg>
    </div>
    <div class="contact-line">DornickAssociates.example
      <svg class="contact-icon" viewBox="0 0 12 12"><circle cx="6" cy="6" r="5.2" fill="none" stroke="#fff"/><path d="M1 6 H11 M6 1 V11" stroke="#fff" fill="none"/></svg>
    </div>
  </div>
</section>

<section class="card card-back">
  <div class="brand">
    <span class="brand-mark"></span>
    <span class="brand-name">Dornick and Associates</span>
  </div>
  <div class="address-band">5173 Wexbury Road Larkmoor Valley 00390-4412</div>
</section>

</body>
</html>
```